Management Consulting firm needs business model Infographic

Belonging Builders is a diversity and inclusion consulting firm. We engage in strategy development, knowledge transfer, and coaching. Our primary colors are red (f02e25), black (241e20), grey (c7c8ca) and white (ffffff) that can be highlighted with (ED7F21), (158A8F) and (1ABB24).

We are looking for a graphical representation of the Belonging Builders business model. We describe what we do as addressing Diversity & Inclusion challenges and opportunities through Relevant Knowledge, Customized Strategies and Measurable Results. Our tagline is: D&I Models, Assessments and Tools for You!

We believe our business model has three stages or phases.
1. Diversity & Inclusion business challenges or opportunities arise such as changing demographics, lost market share, declining revenue, stalled innovation, attracting and retaining top talent, next-generation leadership development, abusive behavior in the workplace, etc.
2. These challenges or opportunities motivate an organization to re-examine the work culture their behaviors create, particularly the mindset, knowledge set and skillset of organizational executives
3. We develop models, assessments and tools that determine and leverage what the organization has been culturally and identify the strategies, action plans, and metrics it needs to address that business challenge or seize those business opportunity.
Thus a client can expect Belonging Builders to generate Relevant Knowledge, Customized Strategies and Measurable Results.

The designer can visit our website https://www.belongingbuilders-example.com/ , and read a blog post https://www.belongingbuilders-example.com/blog-news-cultural-diversity/leading-inclusively-how-cultural-competence-aids-performance for background.

The ideal infographic is one where a portion of it (or in totality) can be used as a Pagebook, WorkLoop and Chirper profile banner.

We have includes some sample infographics that we like.
1) The first is within a SlideMaker deck, Slide 1 is the original infographic template and slide 2 is an example of how BB business model could be added.
2) The other three are also styles we like.

Target Market(s)

Business executives

Industry/Entity Type

Management Consulting

Font styles to use
Sans Serif
Other font styles liked:
• Lato

Colors
ec1f27
000000
474747
0392cd
00a990
9bcb3b

Requirements
Must have
• We are looking for a graphical representation of the Belonging Builders business model. The design must the four components describing what we do: 1) An organization facing a Diversity & Inclusion challenge or opportunity. We address that challenge or opportunity through 2) Relevant Knowledge, 3) Customized Strategies and 4) Measurable Results.
• The design must include the tagline: D&I Models, Assessments and Tools for You!
• We prefer a horizontal / landscape.
Nice to have
• A nice to have is if the design (either in whole, or part) can be used on Pagebook, Chirper or WorkLoop profile banners
• Another nice to have is if the business challenges/opportunities component of the infographic includes examples such as changing demographics, lost market share, declining revenue, stalled innovation, attracting and retaining top talent, next-generation leadership development, abusive behavior in the workplace, etc.
• A nice to have is if the design (either in whole, or part) can be used on the back of a business a card
Should not have
• Silly, unprofessional or business pictures, or icons.

```html
<!DOCTYPE html>
<html lang="en">
<head>
<meta charset="utf-8">
<title>Belonging Builders – D&amp;I Business Model</title>
<link rel="stylesheet" href="https://fonts.googleapis.com/css2?family=Anton&family=Roboto:wght@400;500;700&display=swap">
<style>
  :root {
    --red: #ec1f27;
    --black: #241e20;
    --grey: #c7c8ca;
    --panel: #efefef;
    --white: #ffffff;
    --blue: #0392cd;
    --teal: #00a990;
    --lime: #9bcb3b;
    --icon-shade: rgba(0, 0, 0, 0.28);
  }
  html, body {
    margin: 0;
    padding: 0;
    width: 1200px;
    height: 848px;
    overflow: hidden;
    background: var(--white);
  }
  .model-canvas {
    display: block;
    width: 1200px;
    height: 848px;
  }
  .tagline {
    font-family: "Anton", "Oswald", sans-serif;
    font-size: 60px;
    fill: var(--black);
  }
  .segment-title {
    font-family: "Anton", "Oswald", sans-serif;
    font-size: 23px;
    fill: var(--white);
    letter-spacing: 0.5px;
  }
  .segment-item {
    font-family: "Roboto", Arial, sans-serif;
    font-size: 10px;
    fill: var(--white);
    text-anchor: middle;
  }
  .pillar-label {
    font-family: "Roboto", Arial, sans-serif;
    font-size: 14.5px;
    fill: var(--black);
    text-anchor: middle;
  }
  .brand-name {
    font-family: "Anton", "Oswald", sans-serif;
    font-size: 34px;
    fill: var(--black);
  }
  .leader { stroke: var(--white); stroke-width: 1.2; fill: none; }
  .shade { fill: var(--icon-shade); }
  .shade-line { stroke: var(--icon-shade); stroke-width: 3; fill: none; stroke-linecap: round; }
  .pillar-ring { fill: var(--white); stroke: var(--black); stroke-width: 3; }
  .pillar-arc { fill: none; stroke: var(--red); stroke-width: 6; }
</style>
</head>
<body>
<svg class="model-canvas" viewBox="0 0 850 600" xmlns="http://www.w3.org/2000/svg">
  <defs>
    <linearGradient id="meetingTone" x1="0" y1="0" x2="1" y2="1">
      <stop offset="0" stop-color="#2c3d6e"/>
      <stop offset="1" stop-color="#1f6fb0"/>
    </linearGradient>
  </defs>

  <!-- Tagline panel -->
  <g class="tagline-panel">
    <rect x="309" y="63" width="505" height="232" rx="32" fill="none" stroke="var(--red)" stroke-width="6"/>
    <rect x="300" y="70" width="505" height="232" rx="30" fill="var(--panel)" stroke="var(--black)" stroke-width="4"/>
    <text class="tagline" x="478" y="140" textLength="298" lengthAdjust="spacingAndGlyphs">D&amp;I MODELS,</text>
    <text class="tagline" x="478" y="210" textLength="312" lengthAdjust="spacingAndGlyphs">ASSESSMENTS &amp;</text>
    <text class="tagline" x="478" y="279" textLength="298" lengthAdjust="spacingAndGlyphs">TOOLS FOR YOU!</text>
  </g>

  <!-- Stakeholder wheel -->
  <g class="stakeholder-wheel">
    <path d="M243,262 L18,262 A225,225 0 0 1 243,37 Z" fill="var(--teal)"/>
    <path d="M246,265 L246,40 A225,225 0 0 1 471,265 Z" fill="var(--blue)"/>
    <path d="M246,265 L471,265 A225,225 0 0 1 246,490 Z" fill="var(--red)"/>
    <path d="M243,268 L243,493 A225,225 0 0 1 18,268 Z" fill="var(--lime)"/>

    <!-- Central meeting illustration area -->
    <rect x="152" y="190" width="133" height="170" rx="14" fill="url(#meetingTone)" opacity="0.9"
          role="img" aria-label="Illustration of a business team meeting around a table beside a presentation easel"/>

    <!-- Employee -->
    <text class="segment-title" x="143" y="111">EMPLOYEE</text>
    <path class="leader" d="M140,118 H230"/>
    <path class="shade-line" d="M150,150 A13,13 0 0 1 176,150"/>
    <path class="shade-line" d="M163,150 L170,140"/>
    <text class="segment-item" x="160" y="170">Engagement</text>
    <text class="segment-item" x="160" y="182">Performance</text>
    <path class="shade" d="M80,178 l3,6 7,1 -5,5 1,7 -6,-3 -6,3 1,-7 -5,-5 7,-1z"/>
    <path class="shade" d="M98,182 l2,4 5,1 -4,3 1,5 -4,-2 -4,2 1,-5 -4,-3 5,-1z"/>
    <rect class="shade" x="80" y="202" width="22" height="8" rx="3"/>
    <text class="segment-item" x="88" y="230">Talent</text>
    <text class="segment-item" x="88" y="242">Management</text>

    <!-- Community challenges -->
    <text class="segment-title" x="258" y="122">COMMUNITY</text>
    <text class="segment-title" x="258" y="147">CHALLENGES</text>
    <path class="leader" d="M258,153 H372"/>
    <circle class="shade-line" cx="312" cy="176" r="10"/>
    <path class="shade-line" d="M319,183 L328,193"/>
    <text class="segment-item" x="316" y="216">Recruiting</text>
    <path class="shade" d="M378,178 h8 l14,-9 v26 l-14,-9 h-8z"/>
    <text class="segment-item" x="390" y="211">Advocacy</text>
    <rect class="shade" x="398" y="236" width="5" height="10"/>
    <rect class="shade" x="406" y="230" width="5" height="16"/>
    <rect class="shade" x="414" y="224" width="5" height="22"/>
    <path class="shade-line" d="M397,228 L410,218 L424,214"/>
    <text class="segment-item" x="412" y="262">Economic</text>
    <text class="segment-item" x="412" y="274">Development</text>

    <!-- Customer -->
    <text class="segment-title" x="45" y="306">CUSTOMER</text>
    <path class="leader" d="M45,313 H150"/>
    <rect class="shade" x="74" y="350" width="30" height="18" rx="2"/>
    <text class="segment-item" x="88" y="384">Sales</text>
    <path class="shade" d="M137,372 h6 v16 h-6z M145,388 v-14 l6,-10 h3 v8 h8 v16z"/>
    <text class="segment-item" x="148" y="423">Satisfaction</text>
    <rect class="shade" x="203" y="400" width="26" height="20" rx="3"/>
    <text class="segment-item" x="216" y="441">Loyalty</text>

    <!-- Business partner -->
    <text class="segment-title" x="350" y="313">BUSINESS</text>
    <text class="segment-title" x="350" y="337">PARTNER</text>
    <path class="leader" d="M300,345 H430"/>
    <path class="shade" d="M280,372 h10 a4,4 0 0 1 8,0 h10 v10 a4,4 0 0 1 0,8 v10 h-28z"/>
    <text class="segment-item" x="292" y="411">Collaboration</text>
    <circle class="shade" cx="378" cy="380" r="14"/>
    <path d="M380,370 l-7,12 h6 l-3,9 8,-12 h-6z" fill="var(--red)"/>
    <text class="segment-item" x="378" y="411">Efficiency</text>
    <circle class="shade-line" cx="300" cy="445" r="8"/>
    <circle class="shade" cx="300" cy="445" r="3"/>
    <text class="segment-item" x="300" y="473">Service</text>
  </g>

  <!-- Value pillars -->
  <g class="value-pillars">
    <g class="pillar">
      <path class="pillar-arc" d="M510,320 A48,48 0 0 1 510,416"/>
      <circle class="pillar-ring" cx="510" cy="368" r="42"/>
      <path d="M490,382 q10,-6 20,0 q10,-6 20,0 v10 q-10,-6 -20,0 q-10,-6 -20,0z" fill="var(--blue)"/>
      <circle cx="510" cy="352" r="10" fill="var(--lime)"/>
      <rect x="506" y="362" width="8" height="8" fill="var(--black)"/>
      <text class="pillar-label" x="510" y="451">Relevant</text>
      <text class="pillar-label" x="510" y="469">Knowledge</text>
    </g>
    <g class="pillar">
      <path class="pillar-arc" d="M632,320 A48,48 0 0 1 632,416"/>
      <circle class="pillar-ring" cx="632" cy="368" r="42"/>
      <g stroke="var(--blue)" stroke-width="2.5">
        <path d="M632,368 L632,340 M632,368 L657,368 M632,368 L632,396 M632,368 L607,368 M632,368 L651,349 M632,368 L613,387 M632,368 L651,387 M632,368 L613,349"/>
      </g>
      <g fill="var(--blue)">
        <circle cx="632" cy="340" r="4"/><circle cx="657" cy="368" r="4"/>
        <circle cx="632" cy="396" r="4"/><circle cx="607" cy="368" r="4"/>
        <circle cx="651" cy="349" r="4"/><circle cx="613" cy="387" r="4"/>
        <circle cx="651" cy="387" r="4"/><circle cx="613" cy="349" r="4"/>
      </g>
      <circle cx="632" cy="368" r="11" fill="var(--blue)" stroke="var(--white)" stroke-width="3"/>
      <text class="pillar-label" x="632" y="451">Customized</text>
      <text class="pillar-label" x="632" y="469">Strategies</text>
    </g>
    <g class="pillar">
      <path class="pillar-arc" d="M757,320 A48,48 0 0 1 757,416"/>
      <circle class="pillar-ring" cx="757" cy="368" r="42"/>
      <g fill="var(--blue)">
        <rect x="737" y="375" width="7" height="14"/>
        <rect x="747" y="367" width="7" height="22"/>
        <rect x="757" y="360" width="7" height="29"/>
        <rect x="767" y="351" width="7" height="38"/>
      </g>
      <path d="M735,368 L752,352 L762,358 L778,341" fill="none" stroke="var(--lime)" stroke-width="3"/>
      <path d="M771,340 L780,339 L779,348z" fill="var(--lime)"/>
      <text class="pillar-label" x="757" y="451">Measurable</text>
      <text class="pillar-label" x="757" y="469">Results</text>
    </g>
  </g>

  <!-- Brand name -->
  <g class="brand">
    <text class="brand-name" x="572" y="526">Belonging</text>
    <text class="brand-name" x="572" y="560">Builders</text>
  </g>
</svg>
</body>
</html>
```